Brisvane Partners Web Design

Dear all
I need a web design for a financial services site. We are a broker who deals with many different financial institutions and require a clean, simple and instantly impressive site based on the colour scheme that Mockwell created for us. A landing page (www.brisvn.mx) gives an idea of the logo and clour scheme but we are looking at either a one page site with rollover text boxes or a 3 or 4 page site depending on the preference of the designer and the best user experience. The site“s purpose is to give confidence that the company exists rather than impart pages of information although we would like this to be a site that can expand over time as the company grows. For now the requirement is for a clear set of possibly changing images at the centre of a white screen that relate to finance in general nad the benefits of wealth creation as well as sectios either along the top or bottom - Our Company, Our Approach, Our services, Our clients, Contact (user to fill in contact box to be sent to info@brisvn.mx. The text for each of these boxes I assume can be added by the coding team here, it the overall look and feel that I am looking for from Mockwell - deadline can be extended if necessary but I was hoping to wrap this all up in October

Target Market(s)

Succesful individuals looking to maximise returns on their investment via world class financial institutions and supported throughout by qualified independent financial advisors

Industry/Entity Type

Finance

Requirements
Must have
• Logo and color scheme of the logo design Mockwell sent - I have all these sourcefiles, pantone and fonts

```html
<!DOCTYPE html>
<html lang="en">
<head>
<meta charset="utf-8">
<title>Brisvane Partners</title>
<link href="https://fonts.googleapis.com/css2?family=Federo&family=Arimo:wght@400;700&family=Raleway:wght@500;600;700&display=swap" rel="stylesheet">
<style>
:root{
  --navy:#183764;
  --navy-deep:#13305a;
  --royal:#163f8f;
  --orange:#f0a53c;
  --orange-light:#f7c36d;
  --orange-dark:#e08f22;
  --ink:#222;
  --grey:#555;
  --muted:#999;
  --page:#f4f3f4;
  --line:#e3e3e3;
  --black:#000;
  --footer-text:#8a8a8a;
  --link:#2d6fd8;
  --tweet:#3bb5ec;
}
*{box-sizing:border-box;margin:0;padding:0}
html,body{width:1200px;height:2456px;overflow:hidden}
body{position:relative;background:var(--page);font-family:"Arimo",Arial,sans-serif;color:var(--ink)}
.abs{position:absolute}

/* header */
.site-header{position:absolute;left:0;top:0;width:1200px;height:154px;background:#efefef}
.header-box{position:absolute;left:101px;top:0;width:996px;height:154px;background:#fff}
.brand{position:absolute;left:10px;top:98px;display:flex;align-items:center;gap:14px}
.brand-mark{width:26px;height:26px;background:var(--navy);border-radius:50%}
.brand-name{font-family:"Federo",sans-serif;font-size:26px;line-height:30px;letter-spacing:9px;color:var(--navy)}
.brand-sub{position:absolute;left:66px;top:131px;font-family:"Federo",sans-serif;font-size:8px;letter-spacing:5px;color:var(--navy)}
.call{position:absolute;right:16px;top:24px;font-size:17px;color:#333;line-height:1.3}
.call strong{display:block;font-weight:400;color:var(--orange);font-size:18px}
.search{position:absolute;right:6px;top:98px;width:222px;height:38px;border-radius:19px;background:linear-gradient(#e4e4e4,#f5f5f5);border:1px solid #d3d3d3}
.search svg{position:absolute;left:12px;top:10px}

/* nav */
.main-nav{position:absolute;left:0;top:154px;width:1200px;height:48px;background:linear-gradient(var(--orange-light),var(--orange) 55%,var(--orange-dark));display:flex;align-items:center;padding-left:108px}
.main-nav a{font-family:"Raleway",sans-serif;font-size:15px;color:#fff;text-decoration:none;width:190px;text-align:center;border-left:1px solid rgba(255,255,255,.35);line-height:20px}
.main-nav a.active{background:var(--navy);border:1px solid #fff;border-radius:7px;width:89px;height:36px;line-height:34px;margin-right:30px}
.main-nav a:nth-child(2){border-left:none}

/* hero */
.hero{position:absolute;left:0;top:202px;width:1200px;height:402px;background:var(--navy)}
.hero-frame{position:absolute;left:111px;top:12px;width:611px;height:375px;background:#fff;box-shadow:0 2px 6px rgba(0,0,0,.4)}
.hero-photo{position:absolute;left:14px;top:14px;width:583px;height:347px;background:linear-gradient(90deg,#c9d3dc,#eef1f4 45%,#b8c6d3)}
.hero-copy{position:absolute;left:760px;top:34px;color:#fff}
.hero-copy h1{font-family:"Federo",sans-serif;font-weight:400;font-size:30px;letter-spacing:2px}
.hero-copy h2{font-family:"Federo",sans-serif;font-weight:400;font-size:20px;letter-spacing:2px;margin:6px 0 0 8px;color:#dfe6f0}
.hero-copy .rule{width:290px;height:1px;background:rgba(255,255,255,.25);margin:26px 0 14px}
.sectors{list-style:none}
.sectors li{font-family:"Raleway",sans-serif;font-weight:700;font-size:10.5px;line-height:24px;text-transform:uppercase;padding-left:14px;position:relative}
.sectors li::before{content:"";position:absolute;left:0;top:8px;border-left:5px solid #c8d0dc;border-top:4px solid transparent;border-bottom:4px solid transparent}
.btn-learn{position:absolute;left:0;top:302px;width:186px;height:48px;background:#fff;border-radius:8px;color:var(--navy);font-family:"Federo",sans-serif;font-size:20px;letter-spacing:2px;display:flex;align-items:center;justify-content:center;gap:10px}

/* overview */
.overview{position:absolute;left:101px;top:604px;width:996px;height:472px;background:#fff;border-left:1px solid var(--line);border-right:1px solid var(--line)}
.section-title{position:absolute;width:100%;text-align:center;font-family:"Federo",sans-serif;font-size:33px;letter-spacing:2px;color:var(--navy);font-weight:400}
.ornament{position:absolute;left:50%;margin-left:-80px;width:160px;height:8px}
.intro{position:absolute;width:100%;text-align:center;font-size:13px;line-height:22px;color:var(--grey)}
.device{position:absolute}
.tablet{background:#111;border-radius:10px}
.screen{position:absolute}
.laptop-base{position:absolute;height:16px;background:linear-gradient(#e6e6e6,#999);border-radius:0 0 40px 40px}
.device-label{position:absolute;font-family:"Raleway",sans-serif;font-weight:600;font-size:17px;color:#111;text-align:center;width:260px}

/* blogs */
.blog-card{position:absolute;top:1239px;width:301px;height:490px;background:#fff;border:1px solid #ececec}
.blog-photo{height:200px}
.blog-icon{position:absolute;left:128px;top:178px;width:44px;height:44px;border-radius:50%;background:var(--royal);border:3px solid #fff;display:flex;align-items:center;justify-content:center}
.blog-title{position:absolute;top:234px;width:100%;text-align:center;font-family:"Raleway",sans-serif;font-weight:600;font-size:12.5px;line-height:21px;text-transform:uppercase;color:#111}
.blog-meta{position:absolute;top:287px;width:100%;text-align:center;font-size:11px;color:var(--muted)}
.blog-text{position:absolute;top:316px;left:32px;right:32px;text-align:center;font-size:12.5px;line-height:21px;color:var(--grey)}
.blog-more{position:absolute;bottom:0;width:100%;height:50px;border-top:1px solid #ececec;text-align:center;line-height:50px;font-size:11px;color:#888;text-transform:uppercase}
.btn-blog{position:absolute;left:478px;top:1770px;width:221px;height:39px;background:var(--royal);color:#fff;font-size:12px;text-transform:uppercase;text-align:center;line-height:39px}
.shade{position:absolute;left:120px;top:1836px;width:960px;height:20px;background:radial-gradient(ellipse at top,rgba(0,0,0,.12),transparent 70%)}
.tweet{position:absolute;top:1910px;width:1200px;text-align:center;font-size:14px;color:#222}
.tweet span{color:var(--tweet)}

/* footer */
.site-footer{position:absolute;left:0;top:1973px;width:1200px;height:483px;background:var(--black)}
.f-col{position:absolute;top:36px;width:215px;color:var(--footer-text);font-size:11.5px;line-height:18px}
.f-col h3{font-family:"Raleway",sans-serif;font-weight:700;font-size:12.5px;color:#fff;text-transform:uppercase;margin-bottom:24px}
.f-col p{margin-bottom:14px;color:var(--footer-text)}
.f-col a{color:var(--link);text-decoration:none}
.f-col b{color:#fff}
.f-divider{position:absolute;top:30px;width:1px;height:230px;background:#222}
.field{height:32px;background:#2a2a2a;border:1px solid #3a3a3a;margin-bottom:10px;font-size:10px;color:#777;padding:9px 10px;width:210px}
.btn-sub{margin-left:128px;width:82px;height:28px;background:var(--royal);color:#fff;font-size:10.5px;text-transform:uppercase;text-align:center;line-height:28px}
.news-date{color:#fff;font-weight:700}
.f-rule{position:absolute;left:118px;top:302px;width:941px;height:1px;background:#2a2a2a}
.f-links{position:absolute;top:340px;width:1200px;text-align:center;font-size:11px;color:var(--footer-text)}
.f-links a{color:var(--footer-text);text-decoration:none;padding:0 10px;border-left:1px solid #444}
.f-links a:first-child{border:none}
.to-top{position:absolute;left:547px;top:392px;width:82px;height:82px;border-radius:50%;background:#1c1c1c;display:flex;align-items:center;justify-content:center}
</style>
</head>
<body>

<header class="site-header">
  <div class="header-box">
    <div class="brand"><span class="brand-mark"></span><span class="brand-name">BRISVANE</span></div>
    <div class="brand-sub">PARTNERS</div>
    <div class="call">Call Now:<strong>+300 (555) 010</strong></div>
    <div class="search"><svg width="18" height="18" viewBox="0 0 18 18"><circle cx="7" cy="7" r="5" fill="none" stroke="#333" stroke-width="2"/><path d="M11 11l5 5" stroke="#333" stroke-width="2.5"/></svg></div>
  </div>
</header>

<nav class="main-nav">
  <a class="active" href="#">Home</a>
  <a href="#">Our company</a>
  <a href="#">Our Approach</a>
  <a href="#">Our Services</a>
  <a href="#">Our Clients</a>
  <a href="#">Contact Us</a>
</nav>

<section class="hero">
  <div class="hero-frame"><div class="hero-photo" role="img" aria-label="Photo of a smiling businesswoman resting her chin on her hands in a bright office"></div></div>
  <div class="hero-copy">
    <h1>Welcome to BRISVANE</h1>
    <h2>Lorem Ipsum is simply</h2>
    <div class="rule"></div>
    <ul class="sectors">
      <li>Marketing &amp; Analytics</li>
      <li>Biotechnology</li>
      <li>Consumer Internet &amp; Media</li>
      <li>What happened to the future?</li>
      <li>The transparent term sheet</li>
      <li>Advanced machines &amp; intelligence</li>
      <li>Aerospace &amp; Transportation</li>
    </ul>
    <div class="btn-learn">Learn More <svg width="20" height="16" viewBox="0 0 20 16"><path d="M2 2l6 6-6 6M10 2l6 6-6 6" fill="none" stroke="#183764" stroke-width="3"/></svg></div>
  </div>
</section>

<section class="overview">
  <h2 class="section-title" style="top:38px">Firm OverView</h2>
  <svg class="ornament" style="top:91px" viewBox="0 0 160 8"><path d="M0 4h68M92 4h68" stroke="#ddd"/><circle cx="74" cy="4" r="2" fill="none" stroke="#ccc"/><circle cx="80" cy="4" r="2.5" fill="none" stroke="#ccc"/><circle cx="86" cy="4" r="2" fill="none" stroke="#ccc"/></svg>
  <p class="intro" style="top:112px">Suspendisse in ipsum ut magna pharera aliquet non sodales lorem ipsum belit. Donec sed odio dui.<br>Nulla itae elit libero. Nunc nunc nisl, feugiat eget eleifend sit amet, consectetur sed eros.</p>

  <div class="device tablet" style="left:58px;top:239px;width:204px;height:159px">
    <div class="screen" role="img" aria-label="Video still of rows of white boxes with red cubes" style="left:16px;top:10px;width:172px;height:139px;background:linear-gradient(#cfcfcf,#9a9a9a)"></div>
  </div>
  <div class="device" style="left:279px;top:178px;width:419px;height:220px">
    <div style="position:absolute;left:22px;top:0;width:375px;height:220px;background:#c9c9c9;border-radius:10px 10px 0 0;border:2px solid #aaa"></div>
    <div class="screen" role="img" aria-label="Video still with large hand-drawn words and a screen graphic" style="left:40px;top:14px;width:339px;height:200px;background:linear-gradient(90deg,#a9a6a2,#c5c2bd)"></div>
    <div class="laptop-base" style="left:0;top:210px;width:419px"></div>
  </div>
  <div class="device tablet" style="left:714px;top:239px;width:204px;height:159px">
    <div class="screen" role="img" aria-label="Video still of a grid of dollar tiles" style="left:16px;top:10px;width:172px;height:139px;background:linear-gradient(#dcdcdc,#b3b6bb)"></div>
  </div>
  <div class="device-label" style="left:30px;top:418px">YOUR LIFE IN A BOX</div>
  <div class="device-label" style="left:358px;top:418px">WHO WE ARE</div>
  <div class="device-label" style="left:686px;top:418px">WHAT WE DO</div>
</section>

<h2 class="section-title" style="top:1088px;left:0;width:1200px">Our Blogs</h2>
<svg class="ornament" style="top:1141px" viewBox="0 0 160 8"><path d="M0 4h68M92 4h68" stroke="#ddd"/><circle cx="74" cy="4" r="2" fill="none" stroke="#ccc"/><circle cx="80" cy="4" r="2.5" fill="none" stroke="#ccc"/><circle cx="86" cy="4" r="2" fill="none" stroke="#ccc"/></svg>
<p class="intro" style="top:1161px;left:270px;width:660px">Fringilla ac eros at risus nec Vestibulum montes fames nulla elit. Ipsum Donec Nulla tellus vitae parturi-ent ut elit quis justo Aenean. Nibh at pharetra magna sit ante vitae at In netus orci.</p>

<article class="blog-card" style="left:118px">
  <div class="blog-photo" role="img" aria-label="Photo of people working on laptops in a lounge" style="background:linear-gradient(#8c8f86,#5a5650)"></div>
  <div class="blog-icon"><svg width="14" height="18" viewBox="0 0 14 18"><rect x="4" y="1" width="6" height="10" rx="3" fill="#fff"/><path d="M2 8a5 5 0 0 0 10 0M7 13v4" stroke="#fff" stroke-width="1.6" fill="none"/></svg></div>
  <h3 class="blog-title">Financial Considerations<br>for 2013</h3>
  <p class="blog-meta">Jan 22, 2012 - 19 Comments</p>
  <p class="blog-text">Suspendisse in lorem ipsum ut magna pharera aliquet non sodales lorem ipsum belit. Donec sed odio dui. Nulla lorem itae elit libero. Nunc nunc nisl, feugiat eget eleifend sit amet.</p>
  <div class="blog-more">Read more...</div>
</article>
<article class="blog-card" style="left:439px">
  <div class="blog-photo" role="img" aria-label="Photo of a presenter in a classroom with a projector screen" style="background:linear-gradient(#b9b3a4,#4d4a45)"></div>
  <div class="blog-icon"><svg width="14" height="18" viewBox="0 0 14 18"><rect x="4" y="1" width="6" height="10" rx="3" fill="#fff"/><path d="M2 8a5 5 0 0 0 10 0M7 13v4" stroke="#fff" stroke-width="1.6" fill="none"/></svg></div>
  <h3 class="blog-title">Secrets to a no cost mortgage<br>refinance by Ren D. Marsh, CFP</h3>
  <p class="blog-meta">Jan 22, 2011 - 19 Comments</p>
  <p class="blog-text">Nunc nunc nisl, feugiat eget eleifend sit amet, consectetur sed eros. Qliquam a nisl justo, consectetur sed eros. Qliquam a nisl justo. Suspendisse in lorem ipsum ut magna pharera aliquet.</p>
  <div class="blog-more">Read more...</div>
</article>
<article class="blog-card" style="left:758px">
  <div class="blog-photo" role="img" aria-label="Photo of a speaker addressing a full lecture hall" style="background:linear-gradient(#6b5a52,#7a3b2c)"></div>
  <div class="blog-icon"><svg width="14" height="18" viewBox="0 0 14 18"><rect x="4" y="1" width="6" height="10" rx="3" fill="#fff"/><path d="M2 8a5 5 0 0 0 10 0M7 13v4" stroke="#fff" stroke-width="1.6" fill="none"/></svg></div>
  <h3 class="blog-title">Big spenders vs.<br>big savers</h3>
  <p class="blog-meta">Jan 22, 2011 - 19 Comments</p>
  <p class="blog-text">Lorem ipsum dolor sit amet, consecteaur adipiscing elit. In fringilla sapien ac enim pharetra gravida. Sed lorem ullamcorper bulputate a nisl justo, consectetur sed eros.</p>
  <div class="blog-more">Read more...</div>
</article>

<div class="btn-blog">Read more on our blog</div>
<div class="shade"></div>
<svg class="abs" style="left:581px;top:1863px" width="38" height="38" viewBox="0 0 38 38"><circle cx="19" cy="19" r="16" fill="var(--tweet)"/></svg>
<p class="tweet"><span>@Username</span> : This is Pageforge's version of Lorem Ipsum. Proin gravida nibh vel velit auctor aliquet enean sollicitudin</p>

<footer class="site-footer">
  <div class="f-col" style="left:118px">
    <h3>Newsletter</h3>
    <div class="field">Name</div>
    <div class="field">Email</div>
    <div class="btn-sub">Subscribe</div>
  </div>
  <div class="f-divider" style="left:337px"></div>
  <div class="f-col" style="left:349px">
    <h3>About Company</h3>
    <p>Pretium Praesent ut Vivamus Curabitur Donec tellus consequat Quisque tempus felis. Metus neque Cum augue sed nibh lacinia augue.</p>
    <p>Donec sed odio dui. Nulla itae elit libero. Nunc nunc nisl, feugiat eget eleifend sit ame. <a href="#">More info...</a></p>
  </div>
  <div class="f-divider" style="left:576px"></div>
  <div class="f-col" style="left:588px">
    <h3>Latest News</h3>
    <p><span class="news-date">06.13.12</span><br>Donec sed odio dui. Nulla itae elit libero. Nunc nunc nisl, feugiat eget eleifend sit ame.<br><a href="#">Read more...</a></p>
    <p style="border-top:1px solid #333;padding-top:8px"><span class="news-date">06.13.12</span><br>Donec sed odio dui. Nulla itae elit libero. Nunc nunc nisl, feugiat eget eleifend sit ame.<br><a href="#">Read more...</a></p>
  </div>
  <div class="f-divider" style="left:816px"></div>
  <div class="f-col" style="left:828px">
    <h3>Quick Contact</h3>
    <p>Vestibulum sed et justo Vestibulum Vestibulum natoque orci porttitor Proin felis.</p>
    <p><b>Add:</b> 18B - Harbour Row - West End<br><b>Tel:</b> (555) 010 900 9098</p>
  </div>
  <div class="f-divider" style="left:1058px"></div>
  <div class="f-rule"></div>
  <p class="f-links"><a href="#">Terms of Service &amp; Privacy</a><a href="#">Help &amp; FAQ</a><a href="#">Contact Us</a></p>
  <div class="to-top"><svg width="40" height="24" viewBox="0 0 40 24"><path d="M4 20L20 5l16 15" fill="none" stroke="#000" stroke-width="6"/></svg></div>
</footer>

</body>
</html>
```